Create New Bussiness Card For New Shoes Store

Vandrule is a store that sells a variety of skateboard shoes such as Kestro, Mollen etc. we also sell some skateboard and all skateboard accessories.
we like black and white style logo, but also like blue as well.
We are fully assembled with a deck, truck, wheels, and bearings. Add some personality to your board with a fun, graphic skateboard deck. Constructed of thick 7 ply maple,
Target Market(s)
Target audience: 12-40 year old
especially for young man
Industry/Entity Type
Industrial
Contact Information for Business Card
Name: Vandrule
Address1: 2483 Harlow Brisket Rd
City: Corvell
State: Marston
Zip: 48210
Country: US
Phone: 614830296
email: markolvenby@plimmail.test

```html
<!DOCTYPE html>
<html lang="en">
<head>
<meta charset="utf-8">
<title>Vandrule Business Card</title>
<link rel="stylesheet" href="https://fonts.googleapis.com/css2?family=Open+Sans:wght@400;600;700&display=swap">
<style>
  :root {
    --stage: #2b2b2b;
    --card: #ffffff;
    --card-shade: #eef2f5;
    --brand-blue: #2a9fd6;
    --brand-blue-faint: #d7ecf7;
    --band-text: #ffffff;
  }
  * { box-sizing: border-box; margin: 0; padding: 0; }
  html, body {
    width: 1200px;
    height: 997px;
    overflow: hidden;
    background: var(--stage);
    font-family: "Open Sans", Arial, sans-serif;
  }
  .stage {
    position: relative;
    width: 1200px;
    height: 997px;
    display: flex;
    align-items: center;
    justify-content: center;
  }
  .business-card {
    position: relative;
    width: 900px;
    height: 514px;
    background: var(--card);
    border-radius: 26px;
    overflow: hidden;
    box-shadow: 0 20px 50px rgba(0,0,0,.45);
  }
  .name-pattern {
    position: absolute;
    inset: 0;
    background: linear-gradient(150deg, var(--card) 0%, var(--brand-blue-faint) 45%, var(--card-shade) 70%, var(--card) 100%);
    opacity: .55;
  }
  .brand-mark {
    position: absolute;
    top: 92px;
    left: 300px;
    display: flex;
    align-items: center;
    gap: 22px;
  }
  .brand-mark__dot {
    width: 46px;
    height: 46px;
    border: 3px solid var(--brand-blue);
    border-radius: 50%;
  }
  .brand-mark__name {
    font-size: 78px;
    font-weight: 400;
    color: var(--brand-blue);
    letter-spacing: 1px;
    line-height: 1;
  }
  .contact {
    position: absolute;
    display: flex;
    align-items: center;
    gap: 10px;
    font-weight: 700;
    color: var(--brand-blue);
    white-space: nowrap;
  }
  .contact svg { fill: var(--brand-blue); }
  .contact--address {
    right: 40px;
    top: 300px;
    font-size: 22px;
  }
  .contact--phone {
    left: 40px;
    top: 348px;
    font-size: 28px;
  }
  .product-band {
    position: absolute;
    left: 0;
    right: 0;
    top: 396px;
    height: 46px;
    background: var(--brand-blue);
    color: var(--band-text);
    font-weight: 700;
    font-size: 24px;
    letter-spacing: .5px;
    display: flex;
    align-items: center;
    padding-left: 40px;
    white-space: nowrap;
  }
  .tagline {
    position: absolute;
    left: 40px;
    top: 454px;
    font-size: 25px;
    color: var(--brand-blue);
    font-weight: 400;
    white-space: nowrap;
  }
</style>
</head>
<body>
<main class="stage">
  <article class="business-card">
    <div class="name-pattern" role="img" aria-label="Faint repeated store name pattern across the card background"></div>

    <div class="brand-mark">
      <span class="brand-mark__dot"></span>
      <span class="brand-mark__name">Vandrule</span>
    </div>

    <p class="contact contact--address">
      <svg width="22" height="20" viewBox="0 0 22 20" aria-hidden="true"><path d="M11 1 1 10h3v9h5v-6h4v6h5v-9h3z"/></svg>
      2483 Harlow Brisket Rd Corvell, Marston 48210
    </p>

    <p class="contact contact--phone">
      <svg width="28" height="22" viewBox="0 0 28 22" aria-hidden="true"><path d="M2 7c0-3 5-5 12-5s12 2 12 5v2h-6V6H8v3H2zM7 10h14l4 10H3z"/><circle cx="14" cy="15" r="3" fill="#fff"/></svg>
      614830296
    </p>

    <div class="product-band">SKATEBOARD • SKATEBOARD SHOES • SKATEBOARD ACCESSORIES</div>

    <p class="tagline">We are fully assembled with a deck, truck, wheels, &amp; bearings.</p>
  </article>
</main>
</body>
</html>
```